Local Newspaper Quarterly " Meet The Realtor" print ad

I need a new add made up. This was my last ad:
http://www.heraldpostlistings.example/static/pdfs/agents1309/Ar092213%20G10%20006%20Prepress.pdf

I do not really care of Realtor advertisements because they are just so cheesy and rather pompous-like. However, it's a necessary evil
My ads have always been outside of the box and/or visually sharp.
I now have a new company' Vorel Real Estate( I will attach a logo) contact info:
Cale Vorel
Vorel Real Estate
Broker/Owner( this can be somewhere in small print or corner of ad since it's mandatory to have shown
Phone: 304-555-0147
Email: Cale@VorelRealEstate.Example
VorelRealEstate.Example
I would like social icons(FB,Chirper, Boardly! Roomly, Gplus)

Ideas: In my logo font or using the image at the top I envision
Something like:
A
Vorel Real Estate
Of Mind
Body of ad?
Images of Charleston WV as a real light back ground
With 3 or 4 customer reviews chosen by you in this site:
http://webcale.example/think.html

Bottom: contact info and my name in a nice Signature style ??
My agent pic at the bottom right( to be small. I don't want my big head overshadowing the message)

I have yet to think of a tagline for my new company:
I have been thinking of " Luxury Services For All Things Real Estate"

Or nothing at all ??? I don't care for tag lines but then again that's part of the business

Target Market(s)

Higher end homes

Industry/Entity Type

Business

Colors
0f59a5
0392cd
0f0f0f
eaeaea
ffffff

Requirements
Must have
• My logo and colors
Nice to have
• My agent picture and client review.
Should not have
• No typical real estate images like a house or home buyer

```html
<!DOCTYPE html>
<html lang="en">
<head>
<meta charset="utf-8">
<title>Vorel Real Estate – Meet The Realtor</title>
<link href="https://fonts.googleapis.com/css2?family=Arimo:wght@400;700&display=swap" rel="stylesheet">
<style>
  :root {
    --ink: #0f0f0f;
    --blue-deep: #0f59a5;
    --blue-bright: #0392cd;
    --mist: #eaeaea;
    --paper: #ffffff;
    --sketch: #c9d6e8;
    --portrait-warm: #b8804f;
    --portrait-green: #6f7b3c;
    --logo-dark: #2b2f33;
    --caption: #333333;
  }
  html, body {
    margin: 0;
    padding: 0;
    overflow: hidden;
    background: var(--paper);
  }
  .ad {
    position: relative;
    width: 1200px;
    height: 607px;
    overflow: hidden;
    background: var(--paper);
    font-family: "Arimo", Arial, sans-serif;
    color: var(--ink);
  }
  .ad__backdrop {
    position: absolute;
    inset: 0;
    background: linear-gradient(90deg, rgba(201,214,232,0.35) 0%, rgba(234,234,234,0.25) 45%, rgba(201,214,232,0.35) 100%);
  }
  .ad__backdrop svg { position: absolute; inset: 0; }
  .tagline {
    position: absolute;
    top: 22px;
    left: 0;
    width: 100%;
    margin: 0;
    text-align: center;
    font-weight: 400;
    font-size: 46px;
    line-height: 80px;
    white-space: nowrap;
    text-shadow: 0 0 6px var(--paper), 0 0 12px var(--paper);
  }
  .tagline .cap { font-size: 74px; }
  .web-address {
    position: absolute;
    top: 176px;
    left: 0;
    width: 100%;
    margin: 0;
    text-align: center;
    font-weight: 400;
    font-size: 72px;
    line-height: 84px;
    text-shadow: 0 0 8px var(--paper), 0 0 16px var(--paper);
  }
  .contact {
    position: absolute;
    left: 40px;
    top: 358px;
    margin: 0;
    font-style: normal;
    font-size: 32px;
    line-height: 41px;
    white-space: nowrap;
    text-shadow: 0 0 6px var(--paper), 0 0 10px var(--paper);
  }
  .social {
    position: absolute;
    left: 28px;
    top: 528px;
    display: flex;
    gap: 6px;
    margin: 0;
    padding: 0;
    list-style: none;
  }
  .social__item {
    width: 54px;
    height: 48px;
    border-radius: 6px;
    background: var(--blue-deep);
    color: var(--paper);
    font-size: 10px;
    font-weight: 700;
    display: flex;
    align-items: center;
    justify-content: center;
  }
  .reviews {
    position: absolute;
    left: 605px;
    top: 290px;
    width: 572px;
    font-size: 17px;
    line-height: 21px;
  }
  .reviews p { margin: 0 0 16px; }
  .portrait {
    position: absolute;
    left: 859px;
    top: 424px;
    width: 139px;
    height: 141px;
    background: linear-gradient(135deg, var(--portrait-green) 0%, var(--portrait-warm) 55%, #d9c3a5 100%);
  }
  .brand-mark {
    position: absolute;
    left: 1008px;
    top: 424px;
    width: 155px;
    height: 141px;
    background: radial-gradient(circle at 40% 30%, #5a5f66 0%, var(--logo-dark) 70%);
    display: flex;
    align-items: center;
    justify-content: center;
    gap: 8px;
  }
  .brand-mark__dot {
    width: 10px;
    height: 10px;
    border-radius: 50%;
    background: var(--blue-bright);
  }
  .brand-mark__name {
    font-size: 30px;
    font-weight: 700;
    color: var(--blue-bright);
  }
  .credit {
    position: absolute;
    left: 859px;
    top: 570px;
    width: 304px;
    margin: 0;
    text-align: center;
    font-size: 15px;
    line-height: 18px;
    color: var(--caption);
  }
</style>
</head>
<body>
<main class="ad">
  <div class="ad__backdrop" role="img" aria-label="Faint blue line sketches of doors and windows across the background">
    <svg width="1200" height="607" viewBox="0 0 1200 607" aria-hidden="true">
      <g fill="none" stroke="var(--sketch)" stroke-width="2">
        <rect x="20" y="90" width="110" height="170"/>
        <rect x="320" y="95" width="120" height="120"/>
        <rect x="790" y="300" width="150" height="240"/>
        <rect x="960" y="90" width="130" height="200"/>
        <rect x="1080" y="80" width="100" height="220"/>
        <rect x="560" y="470" width="110" height="137"/>
      </g>
    </svg>
  </div>

  <h1 class="tagline"><span class="cap">"L</span>uxury <span class="cap">S</span>ervices For All Things <span class="cap">R</span>eal <span class="cap">E</span>state<span class="cap">"</span></h1>

  <p class="web-address">VorelRealEstate.Example</p>

  <address class="contact">
    Cale Vorel<br>
    Vorel Real Estate<br>
    Phone: 304-555-0147<br>
    Email: Cale@VorelRealEstate.Example
  </address>

  <ul class="social">
    <li class="social__item">Friendly</li>
    <li class="social__item">Chirper</li>
    <li class="social__item">Boardly</li>
    <li class="social__item">Roomly</li>
    <li class="social__item">Circlet</li>
  </ul>

  <section class="reviews">
    <p>Cale was personable and energetic. In the end he got the job done! Thank you Cale!&nbsp;&nbsp; ~ Marla Keating</p>
    <p>I could not have asked for more support in my home search. I have already recommended Cale to a few people thinking about buying a new home.&nbsp; ~Renee Whitfield</p>
  </section>

  <div class="portrait" role="img" aria-label="Portrait photo of agent Cale Vorel seated outdoors"></div>

  <div class="brand-mark">
    <span class="brand-mark__dot"></span>
    <span class="brand-mark__name">Vorel</span>
  </div>

  <p class="credit">Cale Vorel | Broker | Owner</p>
</main>
</body>
</html>
```